Need website redesign!

I have a site, www.pinehavenfitcamp.example

I am looking to have it redesigned to make it simpler, and encourage people who hit the home page to click on a service, opt in, or contact me for more info. Having a video front and center with icons representing the services we offer around it may be a good idea, but I am open to YOUR design. Conversion is my goal. I want it to be friendly, but convey the fun and ENERGY of my bootcamp. Scrolling pics on home page so people can get a feel for our bootcamp is recommended as well.

```html
<!DOCTYPE html>
<html lang="en">
<head>
<meta charset="utf-8">
<title>Pinehaven Fit Camp</title>
<link rel="stylesheet" href="https://fonts.googleapis.com/css2?family=Arimo:ital,wght@0,400;0,700;1,400&display=swap">
<style>
:root{
  --page:#ececec;
  --panel:#ffffff;
  --black:#0b0b0b;
  --red:#b50a0a;
  --bar:#9d9d9d;
  --bar-edge:#c9c9c9;
  --text:#2a2a2a;
  --form:#5d6b5a;
  --link-blue:#1010e6;
  --white:#ffffff;
}
*{margin:0;padding:0;box-sizing:border-box}
html,body{width:1200px;height:2559px;overflow:hidden}
body{position:relative;background:var(--page);font-family:"Arimo",Arial,sans-serif;color:var(--text)}
.abs{position:absolute}

/* sidebar */
.sidebar{left:0;top:0;width:361px;height:837px;background:var(--red)}
.sidebar-top{left:0;top:0;width:361px;height:184px;background:var(--black)}
.sidebar-bottom{left:0;top:747px;width:361px;height:90px;background:var(--black)}
.brand{left:0;top:0;width:361px;height:184px;display:flex;flex-direction:column;align-items:center;justify-content:center;gap:10px}
.brand-name{color:var(--red);font-weight:700;font-size:30px;line-height:1.05;text-align:center;text-transform:uppercase;width:200px}
.brand-url{color:var(--white);font-size:10px;letter-spacing:.5px}
.social{left:86px;top:200px;display:flex;gap:10px}
.social span{display:block;width:40px;height:40px;border-radius:50%;background:var(--white);border:3px solid #d9d9d9}
.nav{right:calc(1200px - 312px);top:318px;text-align:right;list-style:none}
.nav li{font-size:26px;line-height:54px;color:var(--white)}
.nav li.current{color:var(--black);font-style:italic}
.nav-pointer{left:336px;top:326px}

/* panels */
.panel{left:376px;width:732px;background:var(--panel)}
.panel-bar{left:376px;width:732px;background:var(--bar);border-top:2px solid var(--bar-edge);color:var(--white);font-size:26px;letter-spacing:2px;padding-left:50px;display:flex;align-items:center}
.panel-bar.lead{font-size:33px;padding-left:36px}
.photo{position:absolute}
.copy{font-size:13.5px;line-height:20px;text-align:justify}
.copy p{text-indent:24px}

.optin{left:443px;top:694px;width:581px;height:33px;background:var(--form);display:flex;align-items:center;padding:0 6px;gap:10px;font-size:15px;color:#1c1c1c}
.optin .field{width:165px;height:22px;background:var(--white)}
.optin .send{background:var(--black);color:var(--white);padding:2px 8px;font-size:16px;margin-left:auto}

.video-title{left:416px;top:1090px;color:var(--white);font-size:15px}
.video-controls{left:402px;top:1370px;width:409px;height:40px;background:#1e1e1e}
.watch-btn{left:837px;top:1305px;width:245px;height:36px;background:var(--link-blue);color:var(--white);font-size:20px;display:flex;align-items:center;justify-content:center}

.schedule{left:832px;top:1572px;width:240px;font-size:13px;line-height:22px;text-align:justify}
.schedule b{font-weight:700}
.schedule .gap{height:20px}

.rule{left:412px;top:2242px;width:660px;height:1px;background:#cfcfcf}

.footer{left:0;top:2464px;width:1200px;height:95px;background:var(--black)}
.footer-nav{left:0;top:2498px;width:1200px;text-align:center;color:var(--white);font-size:23px;letter-spacing:.5px}
.top-btn{left:1126px;top:2490px;width:46px;height:46px;border-radius:50%;border:2px solid #cfcfcf;color:var(--white);font-size:13px;display:flex;flex-direction:column;align-items:center;justify-content:center;line-height:1}
</style>
</head>
<body>

<!-- sidebar -->
<div class="abs sidebar"></div>
<div class="abs sidebar-top"></div>
<div class="abs sidebar-bottom"></div>
<div class="abs brand">
  <div class="brand-name">Pinehaven Fit Camp</div>
  <div class="brand-url">www.pinehavenfitcamp.example</div>
</div>
<div class="abs social" aria-label="Social links">
  <span aria-label="Social link"></span><span aria-label="Social link"></span><span aria-label="Social link"></span><span aria-label="Social link"></span>
</div>
<ul class="abs nav">
  <li class="current">Home</li>
  <li>Service</li>
  <li>About</li>
  <li>Support/Contact</li>
  <li>Gallery</li>
</ul>
<svg class="abs nav-pointer" width="25" height="40" viewBox="0 0 25 40"><polygon points="25,0 0,20 25,40" fill="#ececec"/></svg>

<!-- panel 1 -->
<div class="abs panel" style="top:64px;height:878px"></div>
<div class="abs panel-bar lead" style="top:95px;height:76px">LOREM &nbsp;IPSUM &nbsp;DOLOR</div>
<div class="photo" role="img" aria-label="Campers working battle ropes in a gym" style="left:397px;top:205px;width:693px;height:473px;background:linear-gradient(180deg,#b9b6b2 0%,#8c2e34 42%,#6d6a68 60%,#3c3b3a 100%)"></div>
<svg class="abs" style="left:397px;top:635px" width="693" height="43" viewBox="0 0 693 43">
  <rect width="693" height="43" fill="#000" opacity=".25"/>
  <polygon points="40,12 22,22 40,32" fill="#ddd"/>
  <polygon points="653,12 671,22 653,32" fill="#ddd"/>
  <rect x="300" y="20" width="22" height="4" fill="#ddd"/><rect x="328" y="20" width="22" height="4" fill="#999"/><rect x="356" y="20" width="22" height="4" fill="#999"/>
</svg>
<div class="abs optin"><span>Name</span><span class="field"></span><span>Email</span><span class="field"></span><span class="send">SEND</span></div>
<div class="abs copy" style="left:410px;top:757px;width:660px">
  <p>Lorem ipsum dolor sit amet, consectetuer adipiscing elit. Vestibulum ante ipsum primis in faucibus orci luctus et ultrices posuere cubilia Curae; Suspendisse potenti. Pellentesque habitant morbi tristique senectus et netus et malesuada fames ac turpis egestas.</p>
  <p>Vestibulum ante ipsum primis in faucibus orci luctus et ultrices posuere cubilia Curae; Vivamus eu orci. Praesent aliquet, neque pretium congue mattis, ipsum augue dignissim ante, ac pretium nisl lectus at magna. Pellentesque et arcu. Integer risus velit, facilisis eget, viverra et, venenatis id, leo. Quisque dictum quam vel neque.</p>
</div>

<!-- panel 2 -->
<div class="abs panel" style="top:970px;height:468px"></div>
<div class="abs panel-bar" style="top:1006px;height:43px">LOREM &nbsp;IPSUM</div>
<div class="photo" role="img" aria-label="Video of a camper sharing weight-loss results" style="left:402px;top:1082px;width:409px;height:328px;background:linear-gradient(180deg,#2a2a2a,#4a3f36 50%,#1a1a1a)"></div>
<div class="abs video-title">Dana R lost 15 pounds in just 17 sessions!</div>
<svg class="abs" style="left:575px;top:1222px" width="62" height="44" viewBox="0 0 62 44"><rect width="62" height="44" rx="8" fill="#111" opacity=".85"/><polygon points="24,12 42,22 24,32" fill="#fff"/></svg>
<div class="abs video-controls"></div>
<svg class="abs" style="left:402px;top:1370px" width="409" height="40" viewBox="0 0 409 40">
  <rect x="0" y="0" width="409" height="3" fill="#555"/><rect x="0" y="0" width="20" height="3" fill="#c00"/>
  <polygon points="14,14 26,20 14,26" fill="#ccc"/>
  <text x="110" y="25" fill="#ccc" font-size="11" font-family="Arimo, sans-serif">0:10 / 3:10</text>
  <rect x="385" y="13" width="14" height="14" fill="none" stroke="#ccc" stroke-width="2"/>
</svg>
<div class="abs copy" style="left:837px;top:1082px;width:233px">
  <p style="text-indent:40px">Lorem ipsum dolor sit amet, consectetuer adipiscing elit. Vestibulum ante ipsum primis in faucibus orci luctus et ultrices posuere cubilia Curae; Suspendisse potenti. Pellentesque habitant morbi tristique senectus et netus et malesuada fames ac turpis egestas.</p>
</div>
<div class="abs watch-btn">WATCH NEXT VIDEOS</div>

<!-- panel 3 -->
<div class="abs panel" style="top:1466px;height:471px"></div>
<div class="abs panel-bar" style="top:1502px;height:46px">LOREM &nbsp;IPSUM</div>
<div class="photo" role="img" aria-label="Campers doing lunges on indoor turf" style="left:410px;top:1579px;width:347px;height:317px;background:linear-gradient(180deg,#d8d6d0 0%,#b8b6b0 40%,#4a8a3a 70%,#3b6e30 100%)"></div>
<div class="abs schedule">
  <b>Cedar Hollow Location</b><br>
  (morning only)<br>
  M-F: 5:30am, 6:30am<br>
  M, W, F: 7:30a, 9:30am<br>
  Yoga: Monday 7pm, Wednesday 6pm<br>
  Dance Cardio: Tuesday 6pm, Thursday 7pm
  <div class="gap"></div>
  <b>Millbrook Location</b><br>
  (morning, evening, weekends!)<br>
  Bootcamp: Morning: M-F 5:30am Eve: M,W 6:30pm Tues, Thurs 6:15pm Weekends: Sat 8am, 9amKids Sports/Agility:M,W 4pm, 5:15pm<br>
  <b>FOR CURRENT MEMBERS ONLY</b>
</div>

<!-- panel 4 -->
<div class="abs panel" style="top:1965px;height:481px"></div>
<div class="abs panel-bar" style="top:2004px;height:43px">LOREM &nbsp;IPSUM</div>
<div class="photo" role="img" aria-label="Camper training with suspension straps" style="left:412px;top:2078px;width:187px;height:138px;background:linear-gradient(180deg,#9a9892,#5c5a56)"></div>
<div class="photo" role="img" aria-label="Campers doing core work on mats" style="left:647px;top:2078px;width:190px;height:138px;background:linear-gradient(180deg,#6aa4c8,#e9a23a 60%,#3a3a3a)"></div>
<div class="photo" role="img" aria-label="Group of campers posing outdoors" style="left:888px;top:2078px;width:184px;height:138px;background:linear-gradient(180deg,#8fb56a,#4d7a3a 60%,#6b5a4a)"></div>
<div class="abs rule"></div>
<div class="abs copy" style="left:410px;top:2262px;width:660px">
  <p>Lorem ipsum dolor sit amet, consectetuer adipiscing elit. Vestibulum ante ipsum primis in faucibus orci luctus et ultrices posuere cubilia Curae; Suspendisse potenti. Pellentesque habitant morbi tristique senectus et netus et malesuada fames ac turpis egestas.</p>
  <p>Vestibulum ante ipsum primis in faucibus orci luctus et ultrices posuere cubilia Curae; Vivamus eu orci. Praesent aliquet, neque pretium congue mattis, ipsum augue dignissim ante, ac pretium nisl lectus at magna. Pellentesque et arcu. Integer risus velit, facilisis eget, viverra et, venenatis id, leo. Quisque dictum quam vel neque.</p>
</div>

<!-- footer -->
<div class="abs footer"></div>
<div class="abs footer-nav">HOME &nbsp;|&nbsp; SERVICE &nbsp;|&nbsp; ABOUT &nbsp;|&nbsp; CONTACT &nbsp;|&nbsp; GALLERY</div>
<div class="abs top-btn"><svg width="14" height="8" viewBox="0 0 14 8"><polygon points="7,0 14,8 0,8" fill="#fff"/></svg><span style="margin-top:3px">Top</span></div>

</body>
</html>
```